Modern Lawfirm Business Card Design

We're looking for a business card to incorporate the newly created logo we had made.

Ideally looking for a law firm business card demonstrating, modern, minimalist, strong/bold design.

I'm open to any design honestly, but nothing "flashy".

Target Market(s)

Immigration law, family immigration, humanitarian, general legal

Industry/Entity Type

Law Firm

Contact Information for Business Card

Please use dummy information, name, street address, city, state, phone number, email, website.

Font styles to use
Serif
Sans Serif

Requirements
Must have
• Please use dummy information, name, street address, city, state, phone number, email, website.

```html
<!DOCTYPE html>
<html lang="en">
<head>
<meta charset="utf-8">
<title>Valcourt Immigration Law — Business Card</title>
<link rel="stylesheet" href="https://fonts.googleapis.com/css2?family=Roboto:wght@400;500&display=swap">
<style>
  :root {
    --bg: #5f6469;
    --brand-blue: #1a62a3;
    --band-blue: #3a80c6;
    --paper: #ffffff;
    --ink: #1c1c1c;
    --card-w: 540px;
    --card-h: 309px;
  }
  * { margin: 0; padding: 0; box-sizing: border-box; }
  html, body { width: 1200px; height: 900px; overflow: hidden; }
  body {
    background: var(--bg);
    font-family: "Roboto", Arial, sans-serif;
    display: flex;
    align-items: center;
    justify-content: center;
    gap: 40px;
  }
  .card {
    position: relative;
    width: var(--card-w);
    height: var(--card-h);
    border-radius: 16px;
    overflow: hidden;
    box-shadow: 0 10px 24px rgba(0,0,0,.35);
  }
  .card-art { position: absolute; inset: 0; }

  /* front */
  .card--front { background: var(--paper); }
  .front-logo {
    position: absolute; left: 30px; top: 30px;
    color: var(--brand-blue);
    font-weight: 500; font-size: 26px; letter-spacing: 2px; line-height: 1.15;
    text-transform: uppercase;
  }
  .front-logo small { display: block; font-size: 11px; letter-spacing: 5px; font-weight: 500; }
  .contact-list { position: absolute; left: 30px; top: 128px; list-style: none; }
  .contact-item {
    display: flex; align-items: center; gap: 10px;
    font-size: 15px; color: var(--ink); margin-bottom: 9px;
  }
  .contact-icon { width: 20px; height: 20px; flex: none; }
  .name-band {
    position: absolute; right: 12px; top: 56px; width: 200px;
    color: #fff; text-align: center;
  }
  .name-band .person { font-size: 22px; font-weight: 500; letter-spacing: 1px; }
  .name-band .role { font-size: 12px; letter-spacing: 1px; margin-top: 4px; }
  .address {
    position: absolute; left: 230px; top: 212px;
    color: #fff; font-size: 16px; line-height: 1.35;
  }

  /* back */
  .card--back { background: var(--brand-blue); }
  .back-logo {
    position: absolute; inset: 0;
    display: flex; flex-direction: column; align-items: center; justify-content: center;
    color: #fff; font-weight: 500; text-transform: uppercase;
  }
  .back-logo .firm { font-size: 52px; letter-spacing: 4px; }
  .back-logo .practice { font-size: 15px; letter-spacing: 9px; margin-top: 6px; }
</style>
</head>
<body>

  <section class="card card--front">
    <svg class="card-art" viewBox="0 0 540 309" aria-hidden="true">
      <polygon points="372,0 540,0 540,309 20,309" fill="var(--brand-blue)"/>
      <polygon points="340,40 528,40 528,130 310,130 300,80" fill="var(--band-blue)"/>
      <polygon points="300,80 340,40 340,80" fill="#2f6fb0"/>
    </svg>

    <div class="front-logo">Valcourt<small>Immigration Law</small></div>

    <ul class="contact-list">
      <li class="contact-item">
        <svg class="contact-icon" viewBox="0 0 20 20"><rect width="20" height="20" rx="2" fill="var(--brand-blue)"/><path d="M6 4.5l2 .3.8 3-1.4 1a7 7 0 0 0 3.8 3.8l1-1.4 3 .8.3 2c-.1.9-1 1.5-2 1.4A10 10 0 0 1 4.6 6.5c-.1-1 .5-1.9 1.4-2z" fill="#fff"/></svg>
        123-456-1234
      </li>
      <li class="contact-item">
        <svg class="contact-icon" viewBox="0 0 20 20"><rect width="20" height="20" rx="2" fill="var(--brand-blue)"/><rect x="4" y="6" width="12" height="8" fill="none" stroke="#fff" stroke-width="1.4"/><path d="M4 6l6 5 6-5" fill="none" stroke="#fff" stroke-width="1.4"/></svg>
        yourmail@mail.com
      </li>
      <li class="contact-item">
        <svg class="contact-icon" viewBox="0 0 20 20"><rect width="20" height="20" rx="2" fill="var(--brand-blue)"/><circle cx="10" cy="10" r="5.5" fill="none" stroke="#fff" stroke-width="1.3"/><ellipse cx="10" cy="10" rx="2.4" ry="5.5" fill="none" stroke="#fff" stroke-width="1.1"/><path d="M4.5 10h11" stroke="#fff" stroke-width="1.1"/></svg>
        www.yourweb.com
      </li>
    </ul>

    <div class="name-band">
      <div class="person">JHON DOE</div>
      <div class="role">OWNER</div>
    </div>

    <address class="address" style="font-style:normal">
      482 Harbor Crest Rd<br>Milford TN 37190
    </address>
  </section>

  <section class="card card--back">
    <div class="back-logo">
      <span class="firm">Valcourt</span>
      <span class="practice">Immigration Law</span>
    </div>
  </section>

</body>
</html>
```